House-share and Room Rental Website (With Focus on the Bedroom Landing Page)

Looking for website design for our House-share (executive accommodation) and room rental business.

Our company name is: Lodvenra could also be written as LodVenra or lodvenra. Either is fine .. just looking for a nice clean catchy logo to go with the design.

EXAMPLES
These are examples of other websites in this field that are doing well. this is a kind of baseline.
https://kelbrin.com.au/
https://www.tuvaplex.com/
https://www.nestorvi.com/
https://www.quillsa.net/
https://www.pendlebarrow.com.au/

Our business model is to rent rooms to people looking for high-quality accommodation. We fill the gap between those looking to rent rooms and those with rooms to rent. However, our model is slightly different from those already on the market as we looking to fill a massive gap in the market delivering upmarket rooms for rent.(Executive Accommodation) also in the back end will be coupled with a self management process in the back end.

We offer executive style accommodation that stands out above the rest. With special extras like fire safety.. and management processes that create happier homes. We are looking for a web design package that can help us grow and scale our business. We need a design that is captivating

Our MAIN focus is having a room landing page that stands out from the rest... The core of our business will rely on the promotion of the rooms in a share house... so the whole design relies on the BEDROOM landing page to drive results.

Target Market(s)

We have 2 markets we are aiming at ... the first market is people offering rooms to rent who want the highest rental return. The second market is people looking to rent safe, high-quality rooms, in houses that are well managed and looked after.

Industry/Entity Type

Share Economy

Logo Text

LodVenra

Number of Pages Required

5+ page

Font styles to use
Sans Serif

Colors
3276b5

Requirements
Must have
• A messaging system whereby we can create direct communication between those offering rooms and those looking for rooms.
• A call to action that says " Schedule an Inspection"
• Landing page for promoting rooms
• A home page for showing stock.
• Profile page for those selling rooms
• Profile page for those looking for rooms.
• A scheduling calendar for booking inspections
Nice to have
• Pages where new residents can lock in a room.. pay bond and rents.. and sign contracts
• Notifications
• SMS capabilities in the backend.
Should not have
• No script or handwriting fonts.

```html
<!DOCTYPE html>
<html lang="en">
<head>
<meta charset="utf-8">
<title>Lodvenra – Executive Accommodation for Two</title>
<link rel="stylesheet" href="https://fonts.googleapis.com/css2?family=Questrial&family=Open+Sans:wght@400;600&display=swap">
<style>
  :root {
    --brand: #3276b5;
    --brand-bright: #1e88e5;
    --navy: #1d3b5e;
    --ink: #222;
    --white: #fff;
    --panel: #f2f2f2;
    --hero-dark: #1f1f1f;
    --hero-mid: #4a4a48;
  }
  * { box-sizing: border-box; margin: 0; padding: 0; }
  html, body { width: 714px; height: 1200px; overflow: hidden; background: var(--white); }
  body { position: relative; font-family: "Questrial", sans-serif; color: var(--ink); }

  .site-header { position: absolute; top: 0; left: 0; width: 714px; height: 72px; }
  .brand { position: absolute; left: 18px; top: 16px; display: flex; align-items: center; gap: 8px; }
  .brand-dot { width: 22px; height: 22px; border-radius: 50%; background: var(--brand); }
  .brand-name { font-size: 29px; color: var(--brand); line-height: 1; }
  .header-rule { position: absolute; top: 72px; left: 0; width: 714px; height: 5px; background: var(--brand); }

  .hero { position: absolute; top: 77px; left: 0; width: 714px; height: 450px; overflow: hidden; }
  .hero-photo { position: absolute; inset: 0;
    background: radial-gradient(ellipse 60% 45% at 50% 72%, #6e6e6c 0%, transparent 70%),
                linear-gradient(160deg, var(--hero-mid) 0%, #2e2e2d 45%, var(--hero-dark) 100%); }
  .hero-title { position: absolute; top: 176px; width: 100%; text-align: center; color: var(--white);
    font-size: 27px; letter-spacing: 0.2px; top: 99px; }
  .hero-text { position: absolute; top: 132px; left: 0; width: 100%; text-align: center; color: var(--white);
    font-family: "Open Sans", sans-serif; font-weight: 600; font-size: 10px; line-height: 22.4px; }
  .hero-actions { position: absolute; top: 240px; left: 142px; display: flex; gap: 12px; }
  .btn { display: flex; align-items: center; justify-content: center; height: 36px; border-radius: 6px;
    font-size: 15.5px; text-decoration: none; }
  .btn-outline { width: 204px; background: var(--white); color: var(--brand); border: 2px solid var(--brand); }
  .btn-solid { width: 206px; background: var(--brand); color: var(--white); }
  .hero-arrow { position: absolute; top: 145px; width: 40px; height: 52px; }
  .hero-arrow.prev { left: 18px; }
  .hero-arrow.next { right: 18px; }

  .room-facts { position: absolute; bottom: 0; left: 0; width: 714px; height: 44px; background: rgba(10,10,10,.55);
    display: flex; align-items: center; }
  .fact { position: absolute; display: flex; align-items: center; gap: 8px; }
  .fact svg { width: 34px; height: 34px; }
  .fact-label { display: block; color: var(--brand-bright); font-size: 10.5px; line-height: 13px; }
  .fact-value { display: block; color: var(--white); font-size: 12.5px; line-height: 18px; }

  .related-title { position: absolute; top: 548px; width: 100%; text-align: center; color: var(--brand); font-size: 22px; }
  .room-card { position: absolute; top: 589px; width: 214px; height: 220px; background: var(--panel); }
  .room-photo { position: absolute; top: 0; left: 0; width: 100%; height: 142px;
    background: linear-gradient(135deg, #d9d8d4 0%, #a8a39b 45%, #6d675f 100%); }
  .room-place { position: absolute; top: 117px; left: 0; width: 100%; height: 25px; background: rgba(40,40,40,.72);
    color: var(--white); font-size: 11.5px; text-align: center; line-height: 25px; }
  .room-place span { color: var(--brand-bright); }
  .room-specs { position: absolute; top: 152px; left: 12px; width: 196px; display: grid;
    grid-template-columns: 68px 72px 56px; row-gap: 5px; font-size: 9px; color: var(--brand); }
  .spec { display: flex; align-items: center; gap: 5px; height: 13px; }
  .spec svg { width: 13px; height: 13px; flex: none; }
  .room-btn { position: absolute; top: 193px; left: 56px; width: 95px; height: 18px; border-radius: 9px;
    background: var(--brand); color: var(--white); font-size: 9.5px; text-align: center; line-height: 18px; text-decoration: none; }

  .view-more { position: absolute; top: 836px; left: 270px; width: 172px; height: 36px; border: 2px solid var(--brand);
    border-radius: 6px; color: var(--brand); font-size: 17px; display: flex; align-items: center; justify-content: center; text-decoration: none; }

  .site-footer { position: absolute; top: 986px; left: 0; width: 714px; height: 214px; }
  .footer-band { position: absolute; inset: 0; width: 714px; height: 194px; }
  .footer-col { position: absolute; top: 76px; color: var(--white); }
  .footer-col h3 { font-weight: 400; font-size: 16px; margin-bottom: 8px; }
  .footer-col p, .footer-col a { display: block; font-size: 12.5px; line-height: 17.6px; color: var(--white); text-decoration: none; }
  .footer-contact { left: 11px; }
  .footer-contact p { padding-left: 2px; }
  .footer-links { left: 593px; }
  .footer-brand { position: absolute; top: 86px; left: 198px; display: flex; align-items: center; gap: 14px; }
  .footer-brand .brand-dot { width: 40px; height: 40px; background: var(--white); }
  .footer-brand .brand-name { font-size: 54px; color: var(--white); }
  .footer-bar { position: absolute; top: 194px; left: 0; width: 714px; height: 20px; background: var(--navy);
    color: var(--white); font-family: "Open Sans", sans-serif; font-size: 9px; }
  .footer-bar .copyright { position: absolute; left: 13px; top: 3px; }
  .footer-bar .legal { position: absolute; right: 10px; top: 5px; }
</style>
</head>
<body>
<svg width="0" height="0" style="position:absolute">
  <defs>
    <symbol id="i-speed" viewBox="0 0 34 34"><rect x="3" y="6" width="26" height="20" rx="2" fill="none" stroke="currentColor" stroke-width="2.5"/><path d="M1 28h32" stroke="currentColor" stroke-width="3"/><circle cx="22" cy="12" r="7" fill="currentColor"/><path d="M22 12l3-4" stroke="#222" stroke-width="1.5"/></symbol>
    <symbol id="i-bed" viewBox="0 0 34 34"><path d="M2 8v20M2 22h30v6M32 16v12" stroke="currentColor" stroke-width="3" fill="none"/><circle cx="8" cy="14" r="3" fill="currentColor"/><path d="M12 12h18c2 0 2 3 2 4v4H12z" fill="currentColor"/></symbol>
    <symbol id="i-gender" viewBox="0 0 34 34"><g fill="none" stroke="currentColor" stroke-width="2.5"><circle cx="13" cy="15" r="7"/><circle cx="20" cy="12" r="7"/><path d="M13 22v10M9 28h8M25 7l6-6M26 1h5v5"/></g></symbol>
    <symbol id="i-pin" viewBox="0 0 34 34"><path d="M17 2a9 9 0 0 1 9 9c0 7-9 16-9 16S8 18 8 11a9 9 0 0 1 9-9z" fill="currentColor"/><circle cx="17" cy="11" r="3.5" fill="#fff"/><path d="M6 26c-4 3 2 6 11 6s15-3 11-6" fill="none" stroke="currentColor" stroke-width="2"/></symbol>
    <symbol id="i-bath" viewBox="0 0 34 34"><g fill="none" stroke="currentColor" stroke-width="2.5"><path d="M5 18V6a3 3 0 0 1 6 0"/><path d="M2 18h30v4a7 7 0 0 1-7 7H9a7 7 0 0 1-7-7z" fill="currentColor"/><path d="M10 29l-2 4M24 29l2 4"/></g><path d="M14 8l4 4M18 7l2 2M13 12l2 2" stroke="currentColor" stroke-width="1.5"/></symbol>
    <symbol id="i-bed-sm" viewBox="0 0 34 34"><path d="M2 10v16M2 22h30v4M32 16v10" stroke="currentColor" stroke-width="4" fill="none"/><path d="M4 14h28v8H4z" fill="currentColor"/></symbol>
  </defs>
</svg>

<header class="site-header">
  <div class="brand"><span class="brand-dot"></span><span class="brand-name">lodvenra</span></div>
</header>
<div class="header-rule"></div>

<section class="hero">
  <div class="hero-photo" role="img" aria-label="Photo of a dim modern bedroom with a white bed against a concrete wall"></div>
  <h1 class="hero-title">EXCEUTIVE ACCOMODATION FOR TWO</h1>
  <p class="hero-text">Looking for website design for our Houseshare and room rental business.<br>Our business model is to rent rooms to people looking for high quality<br>accommodation.</p>
  <div class="hero-actions">
    <a class="btn btn-outline" href="#">View More Details</a>
    <a class="btn btn-solid" href="#">Schedule an Inspection</a>
  </div>
  <svg class="hero-arrow prev" viewBox="0 0 40 52"><path d="M38 2L3 26l35 24" fill="none" stroke="#fff" stroke-width="2"/></svg>
  <svg class="hero-arrow next" viewBox="0 0 40 52"><path d="M2 2l35 24L2 50" fill="none" stroke="#3276b5" stroke-width="2"/></svg>

  <div class="room-facts">
    <div class="fact" style="left:12px;color:#fff"><svg><use href="#i-speed"/></svg><div><span class="fact-label">INTERNET SPEED</span><span class="fact-value">2 mbps</span></div></div>
    <div class="fact" style="left:152px;color:#fff"><svg><use href="#i-bed"/></svg><div><span class="fact-label">BED SIZE</span><span class="fact-value">6 by 6</span></div></div>
    <div class="fact" style="left:266px;color:#fff"><svg><use href="#i-gender"/></svg><div><span class="fact-label">GENDER PREFERENCE</span><span class="fact-value">Couple</span></div></div>
    <div class="fact" style="left:414px;color:#fff"><svg><use href="#i-pin"/></svg><div><span class="fact-label">ROOM AREA</span><span class="fact-value">400 sqm</span></div></div>
    <div class="fact" style="left:532px;color:#fff"><svg><use href="#i-bath"/></svg><div><span class="fact-label">BATHROOM TYPE</span><span class="fact-value">Shared</span></div></div>
  </div>
</section>

<h2 class="related-title">Other Related Rooms</h2>

<article class="room-card" style="left:20px">
  <div class="room-photo" role="img" aria-label="Photo of a bed with striped pillows"></div>
  <div class="room-place">AIRWAY HEIGHTS, <span>NY USA</span></div>
  <div class="room-specs">
    <span class="spec"><svg><use href="#i-gender"/></svg>Female</span><span class="spec"><svg><use href="#i-pin"/></svg>400 sqm</span><span class="spec"><svg><use href="#i-bed-sm"/></svg>4 by 6 ft</span>
    <span class="spec"><svg><use href="#i-speed"/></svg>5 mbps</span><span class="spec"><svg><use href="#i-bath"/></svg>Private</span>
  </div>
  <a class="room-btn" href="#">View More</a>
</article>
<article class="room-card" style="left:254px">
  <div class="room-photo" role="img" aria-label="Photo of a bed with striped pillows"></div>
  <div class="room-place">AIRWAY HEIGHTS, <span>NY USA</span></div>
  <div class="room-specs">
    <span class="spec"><svg><use href="#i-gender"/></svg>Female</span><span class="spec"><svg><use href="#i-pin"/></svg>400 sqm</span><span class="spec"><svg><use href="#i-bed-sm"/></svg>4 by 6 ft</span>
    <span class="spec"><svg><use href="#i-speed"/></svg>5 mbps</span><span class="spec"><svg><use href="#i-bath"/></svg>Private</span>
  </div>
  <a class="room-btn" href="#">View More</a>
</article>
<article class="room-card" style="left:487px">
  <div class="room-photo" role="img" aria-label="Photo of a bed with striped pillows"></div>
  <div class="room-place">AIRWAY HEIGHTS, <span>NY USA</span></div>
  <div class="room-specs">
    <span class="spec"><svg><use href="#i-gender"/></svg>Female</span><span class="spec"><svg><use href="#i-pin"/></svg>400 sqm</span><span class="spec"><svg><use href="#i-bed-sm"/></svg>4 by 6 ft</span>
    <span class="spec"><svg><use href="#i-speed"/></svg>5 mbps</span><span class="spec"><svg><use href="#i-bath"/></svg>Private</span>
  </div>
  <a class="room-btn" href="#">View More</a>
</article>

<a class="view-more" href="#">View More</a>

<footer class="site-footer">
  <svg class="footer-band" viewBox="0 0 714 194" preserveAspectRatio="none"><path d="M0 0L358 42L714 0V194H0z" fill="#3276b5"/></svg>
  <div class="footer-col footer-contact">
    <h3>CONTACT US</h3>
    <p>Marlow Street 1234</p>
    <p>NY, Example</p>
    <p>infor@halvesto.com</p>
    <p>www.halvesto.com</p>
  </div>
  <div class="footer-brand"><span class="brand-dot"></span><span class="brand-name">lodvenra</span></div>
  <nav class="footer-col footer-links">
    <h3>QUICK LINKS</h3>
    <a href="#">Bedrooms</a>
    <a href="#">Sitting Rooms</a>
    <a href="#">Homes</a>
  </nav>
  <div class="footer-bar">
    <span class="copyright">© Halvesto Ltd 2019</span>
    <span class="legal">Terms | Privacy Policy</span>
  </div>
</footer>
</body>
</html>
```